Bref créative
tri-fold brochures and business card designs
New Bravoline company selling wall panels
marketing material
New company looking for marketing print material for display in retail locations and tradshows.
Home and Garden
Consumers and B2B retailers
tri-fold brochure and business card designs.
Please review website for ideas www.murelune7k.com.
I have most of images as high resolution. I have similar brochure from partner in Australia but would like to diferentiate a little. Be creative.
This image should be used for business card design, I think looks the best, but you will have to play with the black side color and incorporate the logo with contact info.
here is the brochure cover used from our Australia partner but I would like to include same layout of all images but on the inside of brochure, I will need to upload additional 4 designs.
Also I have my own bullet points.
Plimsora logo and my company logo which should be used on back cover to say Plimsora by my company logo..
Plimsora logo
here is Plimsora logo as jpeg, not sure which is needed.
My front cover bullet points
I would like to see how this image could be incorporated on the front cover of brochure where the Logo is positioned..
Try this image on back cover to see how it looks.
Should have my contact info like on website with my company logo. see website.
Images
I would like to see the look of the image boxes look like my catalogue images with the name and tile inset which I will upload
Plimsora tile design images 1 of 2 zip files
Panel inset tiles zip file 2 of 2
I need the 2 page of front side of brochure to have the ecoproduct info from my website www.murelune7k.com

```html
<!DOCTYPE html>
<html lang="en">
<head>
<meta charset="utf-8">
<title>Plimsora brochure</title>
<link href="https://fonts.googleapis.com/css2?family=Open+Sans:wght@400;600;700&display=swap" rel="stylesheet">
<style>
:root{
  --bg:#3a3431;
  --paper:#ffffff;
  --slate:#4b5660;
  --slate-dark:#3e4852;
  --ink:#4a4a4a;
  --grey-logo:#8a8d90;
  --orange-1:#f08a2e;
  --orange-2:#a5420f;
  --orange-3:#5a1f08;
  --cream:#e8e2d6;
  --shadow:rgba(0,0,0,.45);
}
*{box-sizing:border-box;margin:0;padding:0}
html,body{width:1200px;height:874px;overflow:hidden}
body{background:var(--bg);font-family:"Open Sans",Arial,sans-serif;color:var(--ink);position:relative}
.spread{position:absolute;left:120px;width:660px;height:380px;display:flex;box-shadow:0 6px 18px var(--shadow)}
.spread-outside{top:30px}
.spread-inside{top:455px}
.panel{width:220px;height:100%;position:relative;overflow:hidden;background:var(--paper)}
.panel h2{font-size:11px;font-weight:700;color:var(--ink);margin-bottom:6px}
.body-copy{font-size:6.5px;line-height:1.5;color:var(--ink)}
.body-copy p{margin-bottom:6px}
.about{padding:14px 14px 0}
.photo{position:absolute;left:0;right:0;bottom:0}
.photo-interior{height:205px;background:linear-gradient(160deg,#8f9a86 0%,#5b6350 45%,#2f3229 100%)}
.photo-panels{height:215px;background:radial-gradient(circle at 40% 60%,#f3f1ec 0%,#d9d5cc 55%,#a9a398 100%)}
.photo-orange{background:radial-gradient(ellipse at 55% 45%,var(--orange-1) 0%,var(--orange-2) 50%,var(--orange-3) 100%)}
.photo-bamboo{height:120px;background:linear-gradient(90deg,#c9b24a 0%,#e0c45a 20%,#7e8a2c 40%,#d8b948 60%,#9a8a2a 80%,#e4cf6a 100%)}
.contact-panel{background:var(--slate)}
.logo-box{position:absolute;left:0;right:0;top:70px;height:90px;background:var(--paper);display:flex;align-items:center;padding-left:24px;gap:8px}
.logo-name{font-size:26px;font-weight:400;color:var(--grey-logo);letter-spacing:.5px}
.logo-mark{width:10px;height:10px;background:var(--grey-logo)}
.contact{position:absolute;left:18px;bottom:110px;font-size:7px;line-height:1.6;color:#fff}
.contact p+p{margin-top:8px}
.cover-top{height:95px;background:var(--paper);display:flex;align-items:center;padding-left:30px;gap:8px}
.tagline-bar{background:var(--slate);color:#fff;font-size:10px;font-weight:700;padding:6px 10px;text-align:right}
.cover-photo{position:absolute;left:0;right:0;top:119px;bottom:0}
.bullets{position:absolute;left:14px;top:12px;list-style:none;color:#fff;font-size:7.5px;line-height:1.55}
.bullets li::before{content:"\2022";margin-right:4px}
.tiles{display:grid;grid-template-columns:repeat(3,1fr);gap:8px 8px;padding:14px 14px}
.tile{display:flex;flex-direction:column;align-items:center}
.tile-img{width:100%;height:66px}
.tile-img.t1{background:linear-gradient(135deg,#d8cfc2,#8c7f70)}
.tile-img.t2{background:linear-gradient(135deg,#b9b2a6,#5e564c)}
.tile-img.t3{background:linear-gradient(135deg,#e3ddd2,#a99c8a)}
.tile-name{font-size:6px;color:var(--ink);margin-top:2px}
.eco-head{background:var(--slate);color:#fff;font-size:11px;font-weight:700;padding:10px 14px;margin-top:12px}
.eco-copy{padding:10px 14px}
.cover-card{position:absolute;left:860px;top:215px;width:230px;height:430px}
.cover-card .sheet{position:absolute;inset:0;background:var(--paper);box-shadow:0 6px 18px var(--shadow)}
.cover-card .sheet-back{transform:translate(10px,12px);background:#f2f2f2}
.cover-card .sheet-front{overflow:hidden}
.cover-card .cover-top{height:120px}
.cover-card .logo-name{font-size:30px}
.cover-card .tagline-bar{font-size:11px}
.cover-card .cover-photo{top:147px}
.cover-card .bullets{font-size:8.5px}
</style>
</head>
<body>

<section class="spread spread-outside">
  <div class="panel">
    <div class="about">
      <h2>About Us</h2>
      <div class="body-copy">
        <p>Bravoline brings textured wall panels to homes, shops and offices across the region. Our team works with designers, builders and retailers to turn flat surfaces into lasting features that catch the light.</p>
        <p>Every panel is light, easy to install and ready to paint, so any room can change in a single afternoon.</p>
      </div>
    </div>
    <div class="photo photo-interior" role="img" aria-label="Interior room with a textured feature wall and decorative objects"></div>
  </div>

  <div class="panel contact-panel">
    <div class="logo-box">
      <span class="logo-mark"></span>
      <span class="logo-name">Plimsora</span>
    </div>
    <div class="contact">
      <p>Bravoline, 48 Fennick Rd,<br>PO Box 30417, Alder Quay, ON<br>K2T 4R6</p>
      <p>905-555-0182<br>1-877-555-0139</p>
    </div>
  </div>

  <div class="panel">
    <div class="cover-top">
      <span class="logo-mark"></span>
      <span class="logo-name">Plimsora</span>
    </div>
    <div class="tagline-bar">Bring Your Walls to Life</div>
    <div class="cover-photo photo-orange" role="img" aria-label="Warm orange lit textured wall panel">
      <ul class="bullets">
        <li>Innovative interior wall decor products</li>
        <li>Eco friendly product</li>
        <li>100% Recyclable</li>
        <li>Panels are 50cm x 50cm in size</li>
        <li>12 unique model designs</li>
        <li>Made of sugarcane pulp material</li>
        <li>Panels add dimension to your walls</li>
      </ul>
    </div>
  </div>
</section>

<section class="spread spread-inside">
  <div class="panel">
    <div class="about">
      <h2>About Us</h2>
      <div class="body-copy">
        <p>Founded by people who love good spaces, Bravoline offers a range of panel designs for living rooms, lobbies and display walls. Each design adds depth and rhythm without heavy building work.</p>
        <p>We stock panels for homeowners and trade partners alike and ship quickly to retail locations and trade shows.</p>
      </div>
    </div>
    <div class="photo photo-panels" role="img" aria-label="White sculpted wall panels beside a decorative vase"></div>
  </div>

  <div class="panel">
    <div class="tiles">
      <div class="tile"><div class="tile-img t1" role="img" aria-label="Wave panel design"></div><span class="tile-name">Wave</span></div>
      <div class="tile"><div class="tile-img t2" role="img" aria-label="Ripple panel design"></div><span class="tile-name">Ripple</span></div>
      <div class="tile"><div class="tile-img t3" role="img" aria-label="Dune panel design"></div><span class="tile-name">Dune</span></div>
      <div class="tile"><div class="tile-img t2" role="img" aria-label="Brick panel design"></div><span class="tile-name">Brick</span></div>
      <div class="tile"><div class="tile-img t3" role="img" aria-label="Cube panel design"></div><span class="tile-name">Cube</span></div>
      <div class="tile"><div class="tile-img t1" role="img" aria-label="Leaf panel design"></div><span class="tile-name">Leaf</span></div>
      <div class="tile"><div class="tile-img t3" role="img" aria-label="Stone panel design"></div><span class="tile-name">Stone</span></div>
      <div class="tile"><div class="tile-img t1" role="img" aria-label="Arc panel design"></div><span class="tile-name">Arc</span></div>
      <div class="tile"><div class="tile-img t2" role="img" aria-label="Flow panel design"></div><span class="tile-name">Flow</span></div>
      <div class="tile"><div class="tile-img t1" role="img" aria-label="Grid panel design"></div><span class="tile-name">Grid</span></div>
      <div class="tile"><div class="tile-img t2" role="img" aria-label="Drop panel design"></div><span class="tile-name">Drop</span></div>
      <div class="tile"><div class="tile-img t3" role="img" aria-label="Bloom panel design"></div><span class="tile-name">Bloom</span></div>
    </div>
  </div>

  <div class="panel">
    <div class="eco-head">Eco friendly Wall covering</div>
    <div class="eco-copy body-copy">
      <p>Our panels are made from sugarcane pulp, a renewable plant fibre left over after sugar production. Nothing is cut down to make them.</p>
      <p>The material is fully recyclable and free of harmful glues, so your walls look good and stay kind to the planet.</p>
    </div>
    <div class="photo photo-bamboo" role="img" aria-label="Close-up of sugarcane stalks"></div>
  </div>
</section>

<section class="cover-card">
  <div class="sheet sheet-back"></div>
  <div class="sheet sheet-front">
    <div class="cover-top">
      <span class="logo-mark"></span>
      <span class="logo-name">Plimsora</span>
    </div>
    <div class="tagline-bar">Bring Your Walls to Life</div>
    <div class="cover-photo photo-orange" role="img" aria-label="Warm orange lit textured wall panel">
      <ul class="bullets">
        <li>Innovative interior wall decor products</li>
        <li>Eco friendly product</li>
        <li>100% Recyclable</li>
        <li>Panels are 50cm x 50cm in size</li>
        <li>12 unique model designs</li>
        <li>Made of sugarcane pulp material</li>
        <li>Panels add dimension to your walls</li>
      </ul>
    </div>
  </div>
</section>

</body>
</html>
```